Atelier Greta Voss Coming Soon

Launching a online mid century furniture business. I'm participating in an antiques fair prior to the website launch. I'd like a 1 page flyer that highlights a sampling of some iconic pieces and invites people to check out the website soon. If possible, I'd also like a Word template for a tear sheet (a one page doc that has the company logo and contact info, a picture of the item, a field for description and dimensions). The following is an example of a tear sheet...http://www.kbtcabinetworks.example/uploads/4/8/1/3/4813902/vesper_oak_low_side_chair.pdf. I'd prefer a smaller slot for the image (maybe one side of the page) and a much larger area for description and dimensions (as its vintage furniture I'll need to report on condition).

I've attached a few sample pieces of furniture, the company logo, contact information, and a room that included furniture from the business. The color palette for the business is orange, black, white and gray.

Target Market(s)

Potential Customers.....

Industry/Entity Type

Retail

Font styles to use
Other font styles liked:
• I think the fonts should be similar to the ones used in the logo and the business card (see attached)

Colors
f37122
1b1b1b
ebebeb

Requirements
Must have
• An elegant clean look and feel (although its a mid century furniture business I don't carry kitschy items...just really beautiful classic high-end pieces). It should highlight the beauty of the furniture and provide contact information.

```html
<!DOCTYPE html>
<html lang="en">
<head>
<meta charset="utf-8">
<title>Atelier Greta Voss – Online Mid-Century Furniture Flyer</title>
<link rel="stylesheet" href="https://fonts.googleapis.com/css2?family=Open+Sans:wght@400;700&display=swap">
<style>
  :root {
    --orange: #f37122;
    --black: #1b1b1b;
    --gray: #ebebeb;
    --white: #ffffff;
    --backdrop: #e2e2e2;
    --photo-warm: #a58b6e;
    --photo-dark: #3b3129;
    --icon-gold: #e9b02c;
  }
  html, body {
    margin: 0;
    width: 1200px;
    height: 847px;
    overflow: hidden;
    background: var(--backdrop);
  }
  .canvas {
    position: relative;
    width: 1200px;
    height: 847px;
  }
  .flyer {
    position: absolute;
    left: 302px;
    top: 0;
    width: 596px;
    height: 847px;
    display: block;
    font-family: "Open Sans", Arial, sans-serif;
  }
  .brand-name { fill: var(--black); font-weight: 400; font-size: 22px; letter-spacing: 1px; }
  .eyebrow { fill: var(--black); font-size: 14px; font-weight: 400; }
  .headline { fill: var(--black); font-size: 24px; font-weight: 700; }
  .headline-accent { fill: var(--orange); font-size: 22px; font-weight: 700; }
  .invite { fill: var(--black); font-size: 14.5px; font-weight: 700; }
  .contact-name { fill: var(--orange); font-size: 15px; font-weight: 700; }
  .contact-phone { fill: var(--orange); font-size: 11.5px; font-weight: 700; }
  .contact-line { fill: var(--white); font-size: 11.5px; font-weight: 700; }
</style>
</head>
<body>
<main class="canvas">
  <svg class="flyer" viewBox="0 0 453 643" xmlns="http://www.w3.org/2000/svg">
    <defs>
      <linearGradient id="room-dining" x1="0" y1="0" x2="1" y2="1">
        <stop offset="0" stop-color="#c9b79c"/>
        <stop offset="0.55" stop-color="var(--photo-warm)"/>
        <stop offset="1" stop-color="var(--photo-dark)"/>
      </linearGradient>
      <linearGradient id="room-lounge" x1="0" y1="0" x2="1" y2="1">
        <stop offset="0" stop-color="#cdbfa8"/>
        <stop offset="0.5" stop-color="#8f7a63"/>
        <stop offset="1" stop-color="#463a30"/>
      </linearGradient>
    </defs>

    <!-- sheet -->
    <rect class="sheet" width="453" height="643" fill="var(--white)"/>

    <!-- top-left accent -->
    <polygon class="corner-accent" points="0,0 172,0 0,173" fill="var(--orange)"/>

    <!-- room photographs -->
    <polygon class="photo photo-dining" role="img" aria-label="Photo of a dining room with a dark table, white chairs and framed art on the walls"
             points="160,0 244,126 98,250 0,150 0,120 95,0" fill="url(#room-dining)"/>
    <polygon class="photo photo-lounge" role="img" aria-label="Photo of a lounge with mid-century armchairs, a cabinet bar and a gallery wall"
             points="250,136 362,262 188,388 106,262" fill="url(#room-lounge)"/>

    <!-- brand -->
    <text class="brand-name" x="224" y="39" textLength="222" lengthAdjust="spacingAndGlyphs">ATELIER GRETA VOSS</text>

    <!-- diagonal bands -->
    <polygon class="band band-gray" points="0,533 453,178 453,643 0,643" fill="var(--gray)"/>
    <polygon class="band band-orange" points="0,588 453,223 453,643 0,643" fill="var(--orange)"/>
    <polygon class="band band-black" points="10,643 453,278 453,643" fill="var(--black)"/>

    <!-- headline -->
    <text class="eyebrow" x="14" y="355">ONLINE</text>
    <text class="headline" x="14" y="385">MID-CENTURY</text>
    <text class="headline-accent" x="14" y="420">FURNITURE</text>
    <text class="invite" x="14" y="456">Check out the website soon!</text>

    <!-- contact -->
    <text class="contact-name" x="440" y="485" text-anchor="end">Lena Hartwig</text>
    <text class="contact-phone" x="440" y="524" text-anchor="end">Office  555-014-2090</text>
    <text class="contact-phone" x="440" y="541" text-anchor="end">Mobile 555-017-5176</text>

    <g class="icon icon-mail" transform="translate(219,560)">
      <rect width="24" height="17" rx="1.5" fill="var(--icon-gold)"/>
      <polyline points="0,1 12,10 24,1" fill="none" stroke="#a8791a" stroke-width="1.4"/>
    </g>
    <text class="contact-line" x="254" y="575">lena@ateliergretavoss.example</text>

    <g class="icon icon-search" transform="translate(222,588)">
      <circle cx="13" cy="9" r="7.5" fill="#cfcfcf" stroke="#8a8a8a" stroke-width="2"/>
      <line x1="8" y1="15" x2="1" y2="25" stroke="#3fa0d8" stroke-width="4" stroke-linecap="round"/>
    </g>
    <text class="contact-line" x="254" y="609">www.ateliergretavoss.example</text>
  </svg>
</main>
</body>
</html>
```